Redesign two student school awards

I need to redesign 2 students awards. I need the elements of the letterhead to be incorporated into the Student Awards. I have covered some of the letterhead elements to show just the 4 elements that need to be incorporated: school emblem, school name, "For so much, what shall we repay?", and the 3 coloured ribbon. The awards need to be in colour and the use of the 3 school colours - purple, yellow (gold) and chocolate brown,

I have upload the 2 awards the school presents to students (they are printed on A4 Paper). The first one is the:

(1) Year Adviser Award - this award needs to include the school name; the title: Year Adviser's Award; Award to; Name (where the word is deleted and the office staff type the students name or uploaded names which can be autofilled); for the following achievements; the year (which can be changed an include the day and month (but auto filled); Year Adviser (where the teacher signs their name - see lower left of the award; (also the 5 categories - School Service, Community Service , Sporting Achievements, Leadership, Academic Achievement (these 5 categories must be able to be deleted as a student may receive the Year Adviser's Award for 1 or 2 of the categories)

(2) Principal's Award - all elements of this award need to be included. In this example there's a fake name Dale Foster - this is where the office staff type in the students name or hopefully upload a list of names that are auto filled. The 5 categories need to be retained e.g. School Service, Community Service etc (these can be fixed as they are not deleted; for the following achievements; the year (which can be changed an include the day and month (but auto filled); my name and title,

For the 2 student awards it would be good if the design is in a computer program where the office staff can auto fill students names.

The main goal is to redesign the 2 awards, whilst retaining current elements and include 4 of the elements from the letter head.

Target Market(s)

School students (12 years old to 18 years old)

Industry/Entity Type

Education

Font styles to use
Serif

Requirements
Must have
• The elements and school colours mentioned in the description. Would be helpful if the computer program it is contained in allows for auto fill of student names, date, and for the Year Advisers award any one of the five award categories can be removed. To be printed on A4 paper/card

Colours must contain the school colours as mentioned before and the 4 elements of the letterhead. I am trying to have all our communications and awards contain similar elements.

```html
<!DOCTYPE html>
<html lang="en">
<head>
<meta charset="utf-8">
<title>Ridgeway Memorial High School – Student Awards</title>
<link rel="stylesheet" href="https://fonts.googleapis.com/css2?family=Arimo&family=Questrial&family=Tinos:wght@400;700&display=swap">
<style>
  :root{
    --stage:#b3a2a2;
    --purple:#9b3f8f;
    --brown:#3a1219;
    --gold:#ffec00;
    --white:#ffffff;
    --ink:#111111;
  }
  html,body{margin:0;padding:0;overflow:hidden;}
  .stage{position:relative;width:1200px;height:1093px;background:var(--stage);overflow:hidden;}
  .award{position:absolute;width:328px;height:464px;display:block;}
  .col-1{left:58px}.col-2{left:436px}.col-3{left:814px}
  .row-adviser{top:43px}.row-principal{top:586px}
  .school-name{font-family:"Tinos",serif;font-size:21px;fill:var(--white);}
  .emblem-name{font-family:"Tinos",serif;font-size:19px;font-weight:700;fill:var(--gold);}
  .award-kind{font-family:"Questrial",sans-serif;font-size:23px;fill:var(--gold);font-variant:small-caps;letter-spacing:1px;}
  .award-word{font-family:"Questrial",sans-serif;font-size:31px;fill:var(--gold);letter-spacing:2px;}
  .label{font-family:"Arimo",sans-serif;font-size:21px;fill:var(--ink);}
  .student{font-family:"Arimo",sans-serif;font-size:36px;fill:var(--ink);}
  .category{font-family:"Tinos",serif;font-size:27px;font-weight:700;fill:var(--white);}
  .fine{font-family:"Arimo",sans-serif;font-size:11px;fill:var(--ink);}
  .defs{position:absolute;width:0;height:0;}
</style>
</head>
<body>
<svg class="defs" aria-hidden="true">
  <defs>
    <linearGradient id="bg-orange" x1="0" y1="0" x2="0" y2="1"><stop offset="0.28" stop-color="#fff"/><stop offset="1" stop-color="#ff7f00"/></linearGradient>
    <linearGradient id="bg-green" x1="0" y1="0" x2="0" y2="1"><stop offset="0.28" stop-color="#fff"/><stop offset="1" stop-color="#00a046"/></linearGradient>
    <linearGradient id="bg-blue" x1="0" y1="0" x2="0" y2="1"><stop offset="0.28" stop-color="#fff"/><stop offset="1" stop-color="#00a0e6"/></linearGradient>
    <linearGradient id="bg-violet" x1="0" y1="0" x2="0" y2="1"><stop offset="0.86" stop-color="#fff"/><stop offset="1" stop-color="#7a2cff"/></linearGradient>
    <linearGradient id="bg-magenta" x1="0" y1="0" x2="0" y2="1"><stop offset="0.86" stop-color="#fff"/><stop offset="1" stop-color="#a0007a"/></linearGradient>
    <linearGradient id="bg-pink" x1="0" y1="0" x2="0" y2="1"><stop offset="0.86" stop-color="#fff"/><stop offset="1" stop-color="#f8a0f0"/></linearGradient>

    <g id="three-ribbons">
      <path d="M0 38 C150 28 300 66 552 40 L552 60 C350 76 150 42 0 66 Z" fill="var(--purple)"/>
      <path d="M0 72 C120 44 300 56 552 54 L552 62 C330 66 150 60 0 90 Z" fill="var(--brown)"/>
      <path d="M290 44 C420 58 480 42 552 50 L552 60 C470 54 420 64 290 50 Z" fill="var(--gold)"/>
    </g>

    <g id="title-banner">
      <path d="M78 236 C100 214 132 208 156 214 L176 268 L104 286 L118 252 Z" fill="var(--brown)" stroke="var(--gold)" stroke-width="6" stroke-linejoin="round"/>
      <path d="M474 236 C452 214 420 208 396 214 L376 268 L448 286 L434 252 Z" fill="var(--brown)" stroke="var(--gold)" stroke-width="6" stroke-linejoin="round"/>
      <path d="M124 222 C220 198 332 198 428 222 L400 294 C320 276 232 276 152 294 Z" fill="var(--brown)" stroke="var(--gold)" stroke-width="6" stroke-linejoin="round"/>
    </g>

    <g id="name-tab">
      <path d="M0 0 H325 L305 38 H0 Z" fill="var(--gold)"/>
      <path d="M4 -4 H318 L298 33 H4 Z" fill="var(--brown)"/>
    </g>
  </defs>
</svg>

<main class="stage">

  <!-- Year Adviser's Awards -->
  <svg class="award col-1 row-adviser" viewBox="0 0 552 780" aria-label="Year Adviser's Award, Academic Achievement">
    <rect width="552" height="780" fill="url(#bg-orange)"/>
    <use href="#three-ribbons"/>
    <path d="M380 0 H481 V195 L430 176 L380 195 Z" fill="var(--purple)"/>
    <text class="emblem-name" x="430" y="125" text-anchor="middle">Ridgeway</text>
    <use href="#name-tab" x="38" y="106"/>
    <text class="school-name" x="196" y="128" text-anchor="middle">Ridgeway Memorial High School</text>
    <path d="M58 248 H495 A15 15 0 0 0 510 263 V630 A15 15 0 0 0 495 645 H58 A15 15 0 0 0 43 630 V263 A15 15 0 0 0 58 248 Z" fill="#fff" stroke="var(--gold)" stroke-width="6"/>
    <use href="#title-banner"/>
    <text class="award-kind" x="276" y="248" text-anchor="middle">Year Adviser’s</text>
    <text class="award-word" x="276" y="276" text-anchor="middle">AWARD</text>
    <text class="label" x="276" y="313" text-anchor="middle">Awarded to</text>
    <text class="student" x="276" y="404" text-anchor="middle">«Name»</text>
    <line x1="67" y1="416" x2="485" y2="416" stroke="var(--brown)" stroke-width="1.5"/>
    <text class="label" x="276" y="469" text-anchor="middle">for the following</text>
    <text class="label" x="276" y="493" text-anchor="middle">achievements:</text>
    <path d="M45 519 H500 L496 563 H45 Z" fill="var(--brown)"/>
    <path d="M45 515 H496 L490 558 H45 Z" fill="var(--purple)"/>
    <text class="category" x="276" y="547" text-anchor="middle">✣ ACADEMIC ACHIEVEMENT ✣</text>
    <path d="M58 670 H495 A15 15 0 0 0 510 685 V726 A15 15 0 0 0 495 741 H58 A15 15 0 0 0 43 726 V685 A15 15 0 0 0 58 670 Z" fill="#fff" stroke="var(--purple)" stroke-width="5"/>
    <text class="fine" x="136" y="722">Year Adviser</text>
    <text class="fine" x="382" y="722">2020</text>
  </svg>

  <svg class="award col-2 row-adviser" viewBox="0 0 552 780" aria-label="Year Adviser's Award, Leadership">
    <rect width="552" height="780" fill="url(#bg-green)"/>
    <use href="#three-ribbons"/>
    <path d="M380 0 H481 V195 L430 176 L380 195 Z" fill="var(--purple)"/>
    <text class="emblem-name" x="430" y="125" text-anchor="middle">Ridgeway</text>
    <use href="#name-tab" x="38" y="106"/>
    <text class="school-name" x="196" y="128" text-anchor="middle">Ridgeway Memorial High School</text>
    <path d="M58 248 H495 A15 15 0 0 0 510 263 V630 A15 15 0 0 0 495 645 H58 A15 15 0 0 0 43 630 V263 A15 15 0 0 0 58 248 Z" fill="#fff" stroke="var(--gold)" stroke-width="6"/>
    <use href="#title-banner"/>
    <text class="award-kind" x="276" y="248" text-anchor="middle">Year Adviser’s</text>
    <text class="award-word" x="276" y="276" text-anchor="middle">AWARD</text>
    <text class="label" x="276" y="313" text-anchor="middle">Awarded to</text>
    <text class="student" x="276" y="404" text-anchor="middle">«Name»</text>
    <line x1="67" y1="416" x2="485" y2="416" stroke="var(--brown)" stroke-width="1.5"/>
    <text class="label" x="276" y="469" text-anchor="middle">for the following</text>
    <text class="label" x="276" y="493" text-anchor="middle">achievements:</text>
    <path d="M45 519 H459 L455 563 H45 Z" fill="var(--brown)"/>
    <path d="M45 515 H455 L449 558 H45 Z" fill="var(--purple)"/>
    <text class="category" x="276" y="547" text-anchor="middle">✣ LEADERSHIP ✣</text>
    <path d="M58 670 H495 A15 15 0 0 0 510 685 V726 A15 15 0 0 0 495 741 H58 A15 15 0 0 0 43 726 V685 A15 15 0 0 0 58 670 Z" fill="#fff" stroke="var(--purple)" stroke-width="5"/>
    <text class="fine" x="136" y="722">Year Adviser</text>
    <text class="fine" x="382" y="722">2020</text>
  </svg>

  <svg class="award col-3 row-adviser" viewBox="0 0 552 780" aria-label="Year Adviser's Award, School Service">
    <rect width="552" height="780" fill="url(#bg-blue)"/>
    <use href="#three-ribbons"/>
    <path d="M380 0 H481 V195 L430 176 L380 195 Z" fill="var(--purple)"/>
    <text class="emblem-name" x="430" y="125" text-anchor="middle">Ridgeway</text>
    <use href="#name-tab" x="38" y="106"/>
    <text class="school-name" x="196" y="128" text-anchor="middle">Ridgeway Memorial High School</text>
    <path d="M58 248 H495 A15 15 0 0 0 510 263 V630 A15 15 0 0 0 495 645 H58 A15 15 0 0 0 43 630 V263 A15 15 0 0 0 58 248 Z" fill="#fff" stroke="var(--gold)" stroke-width="6"/>
    <use href="#title-banner"/>
    <text class="award-kind" x="276" y="248" text-anchor="middle">Year Adviser’s</text>
    <text class="award-word" x="276" y="276" text-anchor="middle">AWARD</text>
    <text class="label" x="276" y="313" text-anchor="middle">Awarded to</text>
    <text class="student" x="276" y="404" text-anchor="middle">«Name»</text>
    <line x1="67" y1="416" x2="485" y2="416" stroke="var(--brown)" stroke-width="1.5"/>
    <text class="label" x="276" y="469" text-anchor="middle">for the following</text>
    <text class="label" x="276" y="493" text-anchor="middle">achievements:</text>
    <path d="M45 519 H459 L455 563 H45 Z" fill="var(--brown)"/>
    <path d="M45 515 H455 L449 558 H45 Z" fill="var(--purple)"/>
    <text class="category" x="276" y="547" text-anchor="middle">✣ SCHOOL SERVICE ✣</text>
    <path d="M58 670 H495 A15 15 0 0 0 510 685 V726 A15 15 0 0 0 495 741 H58 A15 15 0 0 0 43 726 V685 A15 15 0 0 0 58 670 Z" fill="#fff" stroke="var(--purple)" stroke-width="5"/>
    <text class="fine" x="136" y="722">Year Adviser</text>
    <text class="fine" x="382" y="722">2020</text>
  </svg>

  <!-- Principal's Awards -->
  <svg class="award col-1 row-principal" viewBox="0 0 552 780" aria-label="Principal's Award, Academic Achievement">
    <rect width="552" height="780" fill="url(#bg-violet)"/>
    <path d="M61 214 H476 A15 15 0 0 0 491 229 V565 A55 55 0 0 1 436 620 H116 A55 55 0 0 1 61 565 V229 A15 15 0 0 0 61 214 Z" fill="#fff" stroke="var(--purple)" stroke-width="5"/>
    <path d="M226 0 H326 V297 L276 280 L226 297 Z" fill="var(--purple)"/>
    <use href="#name-tab" x="113" y="34"/>
    <text class="school-name" x="271" y="57" text-anchor="middle">Ridgeway Memorial High School</text>
    <use href="#title-banner" y="-122"/>
    <text class="award-kind" x="276" y="126" text-anchor="middle">Principal’s</text>
    <text class="award-word" x="276" y="154" text-anchor="middle">AWARD</text>
    <text class="emblem-name" x="276" y="235" text-anchor="middle">Ridgeway</text>
    <text class="label" x="276" y="325" text-anchor="middle">Awarded to</text>
    <text class="student" x="276" y="404" text-anchor="middle">Dale Foster</text>
    <line x1="80" y1="416" x2="472" y2="416" stroke="var(--brown)" stroke-width="1.5"/>
    <text class="label" x="276" y="469" text-anchor="middle">for the following</text>
    <text class="label" x="276" y="493" text-anchor="middle">achievements:</text>
    <path d="M45 535 L33 579 L58 570 Z M507 535 L519 579 L494 570 Z" fill="var(--purple)"/>
    <path d="M45 559 L58 570 L58 559 Z M507 559 L494 570 L494 559 Z" fill="var(--brown)"/>
    <rect x="45" y="515" width="462" height="44" fill="var(--purple)"/>
    <text class="category" x="276" y="546" text-anchor="middle">✣ ACADEMIC ACHIEVEMENT ✣</text>
    <text class="fine" x="136" y="684">Principal:  Mr. K. Whitlow</text>
    <text class="fine" x="382" y="684">2020</text>
    <use href="#three-ribbons" y="665"/>
  </svg>

  <svg class="award col-2 row-principal" viewBox="0 0 552 780" aria-label="Principal's Award, Leadership">
    <rect width="552" height="780" fill="url(#bg-magenta)"/>
    <path d="M61 214 H476 A15 15 0 0 0 491 229 V565 A55 55 0 0 1 436 620 H116 A55 55 0 0 1 61 565 V229 A15 15 0 0 0 61 214 Z" fill="#fff" stroke="var(--purple)" stroke-width="5"/>
    <path d="M226 0 H326 V297 L276 280 L226 297 Z" fill="var(--purple)"/>
    <use href="#name-tab" x="113" y="34"/>
    <text class="school-name" x="271" y="57" text-anchor="middle">Ridgeway Memorial High School</text>
    <use href="#title-banner" y="-122"/>
    <text class="award-kind" x="276" y="126" text-anchor="middle">Principal’s</text>
    <text class="award-word" x="276" y="154" text-anchor="middle">AWARD</text>
    <text class="emblem-name" x="276" y="235" text-anchor="middle">Ridgeway</text>
    <text class="label" x="276" y="325" text-anchor="middle">Awarded to</text>
    <text class="student" x="276" y="404" text-anchor="middle">Dale Foster</text>
    <line x1="80" y1="416" x2="472" y2="416" stroke="var(--brown)" stroke-width="1.5"/>
    <text class="label" x="276" y="469" text-anchor="middle">for the following</text>
    <text class="label" x="276" y="493" text-anchor="middle">achievements:</text>
    <path d="M45 535 L33 579 L58 570 Z M507 535 L519 579 L494 570 Z" fill="var(--purple)"/>
    <path d="M45 559 L58 570 L58 559 Z M507 559 L494 570 L494 559 Z" fill="var(--brown)"/>
    <rect x="45" y="515" width="462" height="44" fill="var(--purple)"/>
    <text class="category" x="276" y="546" text-anchor="middle">✣ LEADERSHIP ✣</text>
    <text class="fine" x="136" y="684">Principal:  Mr. K. Whitlow</text>
    <text class="fine" x="382" y="684">2020</text>
    <use href="#three-ribbons" y="665"/>
  </svg>

  <svg class="award col-3 row-principal" viewBox="0 0 552 780" aria-label="Principal's Award, School Service">
    <rect width="552" height="780" fill="url(#bg-pink)"/>
    <path d="M61 214 H476 A15 15 0 0 0 491 229 V565 A55 55 0 0 1 436 620 H116 A55 55 0 0 1 61 565 V229 A15 15 0 0 0 61 214 Z" fill="#fff" stroke="var(--purple)" stroke-width="5"/>
    <path d="M226 0 H326 V297 L276 280 L226 297 Z" fill="var(--purple)"/>
    <use href="#name-tab" x="113" y="34"/>
    <text class="school-name" x="271" y="57" text-anchor="middle">Ridgeway Memorial High School</text>
    <use href="#title-banner" y="-122"/>
    <text class="award-kind" x="276" y="126" text-anchor="middle">Principal’s</text>
    <text class="award-word" x="276" y="154" text-anchor="middle">AWARD</text>
    <text class="emblem-name" x="276" y="235" text-anchor="middle">Ridgeway</text>
    <text class="label" x="276" y="325" text-anchor="middle">Awarded to</text>
    <text class="student" x="276" y="404" text-anchor="middle">Dale Foster</text>
    <line x1="80" y1="416" x2="472" y2="416" stroke="var(--brown)" stroke-width="1.5"/>
    <text class="label" x="276" y="469" text-anchor="middle">for the following</text>
    <text class="label" x="276" y="493" text-anchor="middle">achievements:</text>
    <path d="M45 535 L33 579 L58 570 Z M507 535 L519 579 L494 570 Z" fill="var(--purple)"/>
    <path d="M45 559 L58 570 L58 559 Z M507 559 L494 570 L494 559 Z" fill="var(--brown)"/>
    <rect x="45" y="515" width="462" height="44" fill="var(--purple)"/>
    <text class="category" x="276" y="546" text-anchor="middle">✣ SCHOOL SERVICE ✣</text>
    <text class="fine" x="136" y="684">Principal:  Mr. K. Whitlow</text>
    <text class="fine" x="382" y="684">2020</text>
    <use href="#three-ribbons" y="665"/>
  </svg>

</main>
</body>
</html>
```